letter flyer TRADEUP

please see our website www.corvellpartners.com.au for details. however, we are a financial services company that has services in accounting and taxation, wealth advice, loan broking, general insurance and business advice. we want to target local potential business clients to focus on helping them conduct a review and work out what they need to do to improve the health and profitability of their business. we would like to create a letter/flyer to send them. we want the message to be as follows:
1) by having a review, we guarantee we will provide some financial benefit;
2) we are offering a cohesive and comprehensive team who will provide many financial services under one roof; and
3) we specialise in business.

we have called the campaign 'TRADEUP'

we have drafted a letter as a concept and we need design, any suggested changes in wording and imagery to demonstrate our message. We do have a logo for each of the divisions above. we thought the reverse side could just be our logo and catchphrase 'financial freedom is...'

***** we just want an A4 letter... not a bifold flyer
***** I have also included a copy of our newsletter so you can get the logos and feel for our business

```html
<!DOCTYPE html>
<html lang="en">
<head>
<meta charset="utf-8">
<title>Corvell Partners – TRADEUP Letter</title>
<link href="https://fonts.googleapis.com/css2?family=Source+Sans+3:wght@400;600;700&display=swap" rel="stylesheet">
<style>
  :root {
    --canvas: #ffffff;
    --blue: #1a5db5;
    --blue-light: #36a0f6;
    --blue-deep: #1050bf;
    --link-blue: #2140b8;
    --white: #ffffff;
    --orange: #e59a2a;
    --brand-grey: #4a5a66;
    --box-text: #1a5db5;
  }
  * { margin: 0; padding: 0; box-sizing: border-box; }
  html, body { width: 1200px; height: 1000px; overflow: hidden; background: var(--canvas); }
  body { position: relative; font-family: "Source Sans 3", Arial, sans-serif; }

  .letter-page {
    position: absolute; left: 5px; top: 98px; width: 567px; height: 800px;
    background: var(--white); overflow: hidden;
  }
  .letter-wave { position: absolute; left: 0; top: 0; width: 567px; height: 675px; }
  .site-url {
    position: absolute; right: 18px; top: 2px;
    color: var(--link-blue); font-size: 17px; font-weight: 400;
  }
  .brand { position: absolute; display: flex; align-items: center; gap: 10px; }
  .brand-dot { width: 46px; height: 46px; border-radius: 50%; background: var(--blue); flex: none; }
  .brand-name {
    color: var(--brand-grey); font-size: 16px; font-weight: 600;
    line-height: 1.05; letter-spacing: 0.5px; text-transform: uppercase;
  }
  .brand-tagline {
    position: absolute; color: var(--orange); font-weight: 700; font-size: 11.5px;
  }
  .letter-page .brand { left: 18px; top: 22px; }
  .letter-page .brand-tagline { left: 50px; top: 104px; }

  .letter-body {
    position: absolute; left: 32px; top: 140px; width: 520px;
    color: var(--white); font-size: 10.6px; line-height: 1.3;
  }
  .salutation { font-size: 24px; font-weight: 400; margin-bottom: 22px; }
  .letter-body ul { list-style: none; }
  .letter-body li { position: relative; padding-left: 13px; }
  .letter-body li::before { content: "•"; position: absolute; left: 0; }
  .q-list li { margin-bottom: 12px; }
  .q-list li:first-child { margin-bottom: 2px; }
  .q-list li:last-child { margin-bottom: 26px; }
  .letter-body p { margin-bottom: 12px; }
  .benefit-list li { margin-bottom: 12px; }
  .voucher { color: var(--orange); font-weight: 700; }

  .health-box {
    position: absolute; left: 26px; top: 546px; width: 528px; height: 122px;
    background: var(--white); border-radius: 12px;
    padding: 7px 8px; color: var(--box-text); font-size: 10.6px; line-height: 1.3;
  }
  .health-box strong { display: block; text-align: center; font-weight: 700; margin-top: 12px; font-size: 11px; }

  .photo-strip { position: absolute; left: 0; top: 674px; width: 567px; height: 126px; }
  .photo { position: absolute; top: 0; height: 126px; }
  .photo-keyboard { left: 0; width: 190px; background: linear-gradient(135deg, #3a3f44, #1c1f22 60%, #5fbf3a); }
  .photo-office { left: 193px; width: 187px; background: linear-gradient(160deg, #b8b2a6, #6e6a62 55%, #2d3440); }
  .photo-money { left: 383px; width: 184px; background: linear-gradient(150deg, #e8e4dc, #5a6470 45%, #c08a3a); }

  .cover-page {
    position: absolute; left: 626px; top: 95px; width: 554px; height: 796px;
    background: linear-gradient(180deg, var(--blue-light), var(--blue-deep));
  }
  .cover-band {
    position: absolute; left: 0; top: 298px; width: 554px; height: 138px; background: var(--white);
  }
  .cover-band .brand { left: 188px; top: 20px; }
  .cover-band .brand-tagline { left: 220px; top: 102px; }
</style>
</head>
<body>

<section class="letter-page">
  <svg class="letter-wave" viewBox="0 0 567 675" aria-hidden="true">
    <path d="M0 137 C150 108 320 60 567 116 L567 675 L0 675 Z" fill="#1a5db5"/>
  </svg>
  <div class="site-url">www.corvellpartners.com.au</div>
  <div class="brand">
    <span class="brand-dot"></span>
    <span class="brand-name">Corvell<br>Partners</span>
  </div>
  <div class="brand-tagline">YOUR WEALTH ADVISORS</div>

  <div class="letter-body">
    <h1 class="salutation">Dear xyz,</h1>
    <ul class="q-list">
      <li>Are you working long hours and feel like you are not reaping the benefits you should be?</li>
      <li>Do you have work life balance?</li>
      <li>Do you understand your businesses strengths and weaknesses?</li>
      <li>Do you feel like you have potential to grow?</li>
    </ul>
    <p>Our business is to help you better understand your business and help you to prepare unique strategies to improve the success and value of your business.</p>
    <p>We can assist to streamline your financial service relationships, providing all financial services under one roof. Such as, accounting and taxation, business planning, wealth planning, smsf, insurance, loan broking, general insurance and business planning. What does this mean for you?:</p>
    <ul class="benefit-list">
      <li>Coordinated approach and one simple phone call to meet your financial requiremnts. This saves you time and effort; and</li>
      <li>A financial services team working together for your business review will ensure you have savings and maximise your financial position with a solid team behind you, all coordinated and on the same team HOW TO TAKE ADVANTAGE OF YOUR INITIAL COMPLIMENTARY BUSINESS CHECK – SIMPLY CALL OR EMAIL US AND QUOTE ‘TRADEUP’.</li>
    </ul>
    <p>IF YOU DO NOT FIND VALUE IN THE DISUCSSION – <span class="voucher">YOU GET A VOUCHER!</span></p>
  </div>

  <div class="health-box">
    Our business health checks are purposefully designed to provide an accurate overview of how your business is travelling, so you can effectively harness this information and take the necessary steps to making your business healthier, more efficient and essentially more profitable. We provide a summary of the main impact on your business and estimate the dollar value so you can see how much you would save if implemented.
    <strong>Start 2016 with a focus on your business health and reap the rewards of having a professional financial services team.</strong>
  </div>

  <div class="photo-strip">
    <div class="photo photo-keyboard" role="img" aria-label="Keyboard with a green Health key"></div>
    <div class="photo photo-office" role="img" aria-label="Businessman working on a laptop in an office lounge"></div>
    <div class="photo photo-money" role="img" aria-label="Calculator resting on coins and banknotes"></div>
  </div>
</section>

<section class="cover-page">
  <div class="cover-band">
    <div class="brand">
      <span class="brand-dot"></span>
      <span class="brand-name">Corvell<br>Partners</span>
    </div>
    <div class="brand-tagline">YOUR WEALTH ADVISORS</div>
  </div>
</section>

</body>
</html>
```